Business Card for Orvane Parts Wholesale supplier

Hi There! I need a new business card for our company. We are specialized in selling Orvane parts, mostly we sell new LCD screens for Telvox and Slatrons. I would like to see that back in the design.

You can find the colors and logo's on our website: www.dorvak-example.nl

Industry/Entity Type

Business

Contact Information for Business Card

My Details:
Lars Vintorp

Phone: 0031612873406
E-mail: Lars@dorvak-example.nl

Slogan: "Because Quality Matters"

Font styles to use
Sans Serif

Colors

Designer to choose colors to be used in the design.

Requirements
Must have
• A Black backside with the Dorvak logo on it. The front side should be clean with only my contact details.
• But I'm also open for something really different or awesome!
Nice to have
• Remember that we are in the parts & repairing industry, So i'll be handing those business cards mainly to repair companies. Maybe you can do something with that thought :)

```html
<!DOCTYPE html>
<html lang="en">
<head>
<meta charset="utf-8">
<title>Dorvak Business Card</title>
<link rel="stylesheet" href="https://fonts.googleapis.com/css2?family=Jost:wght@400;500;600&family=Kaushan+Script&display=swap">
<style>
  :root {
    --page-bg: #e8e8e9;
    --card-white: #f7f7f7;
    --ink-grey: #5d5d5f;
    --ink-dark: #3a3a3c;
    --rule-grey: #8a8a8c;
    --accent-orange: #e0833f;
    --back-light: #6e6e6e;
    --back-dark: #161616;
    --logo-white: #ececec;
    --url-grey: #8c8c8c;
  }
  * { box-sizing: border-box; margin: 0; padding: 0; }
  html, body { width: 1200px; height: 720px; overflow: hidden; }
  body {
    background: var(--page-bg);
    font-family: "Jost", "Futura", sans-serif;
    position: relative;
  }
  .card {
    position: absolute;
    top: 205px;
    width: 500px;
    height: 310px;
    border-radius: 3px;
    box-shadow: 0 10px 30px rgba(0,0,0,0.12);
  }
  .card--front { left: 70px; background: var(--card-white); }
  .card--back {
    left: 630px;
    background: linear-gradient(215deg, var(--back-light) 0%, #3a3a3a 45%, var(--back-dark) 100%);
  }

  .front__identity {
    position: absolute;
    top: 62px;
    left: 0; right: 0;
    text-align: center;
  }
  .front__name {
    font-weight: 600;
    font-size: 27px;
    letter-spacing: 1px;
    color: var(--ink-grey);
  }
  .front__rule {
    width: 48px;
    height: 1px;
    background: var(--rule-grey);
    margin: 12px auto;
  }
  .front__slogan {
    font-family: "Kaushan Script", cursive;
    font-size: 22px;
    color: var(--accent-orange);
  }
  .front__contacts {
    position: absolute;
    left: 34px; right: 30px;
    bottom: 44px;
    display: flex;
    justify-content: space-between;
    align-items: center;
  }
  .contact {
    display: flex;
    align-items: center;
    gap: 10px;
    font-size: 20px;
    color: var(--ink-dark);
  }
  .contact__icon { width: 22px; height: 22px; flex: none; }

  .back__brand {
    position: absolute;
    top: 112px;
    left: 0; right: 0;
    display: flex;
    justify-content: center;
    align-items: center;
    gap: 16px;
  }
  .back__mark {
    width: 46px; height: 46px;
    border-radius: 50%;
    background: var(--accent-orange);
  }
  .back__name {
    font-weight: 500;
    font-size: 62px;
    line-height: 1;
    color: var(--logo-white);
    letter-spacing: 1px;
  }
  .back__url {
    position: absolute;
    bottom: 42px;
    left: 0; right: 0;
    text-align: center;
    font-size: 20px;
    letter-spacing: 1px;
    color: var(--url-grey);
  }
</style>
</head>
<body>
  <section class="card card--front" aria-label="Business card front">
    <div class="front__identity">
      <h1 class="front__name">LARS VINTORP</h1>
      <div class="front__rule"></div>
      <p class="front__slogan">"because quality matters"</p>
      <div class="front__rule"></div>
    </div>
    <div class="front__contacts">
      <div class="contact contact--phone">
        <svg class="contact__icon" viewBox="0 0 24 24" aria-hidden="true">
          <circle cx="12" cy="12" r="10" fill="none" stroke="#e0833f" stroke-width="1.6"/>
          <path d="M9 7.5c-.8.6-1 1.8-.5 3.2.7 2 2.2 3.7 4 4.6 1.2.6 2.3.5 2.9-.2l-1.6-1.6-1.2.7c-1-.5-1.8-1.4-2.2-2.5l.9-1-1.1-2.2z" fill="#e0833f"/>
        </svg>
        <span>003 161-2873406</span>
      </div>
      <div class="contact contact--email">
        <svg class="contact__icon" viewBox="0 0 24 24" aria-hidden="true">
          <rect x="2" y="5" width="20" height="14" rx="1" fill="#e8a86a"/>
          <path d="M2 5l10 8 10-8" fill="none" stroke="#c8702f" stroke-width="1.4"/>
        </svg>
        <span>Lars@dorvak-example.nl</span>
      </div>
    </div>
  </section>

  <section class="card card--back" aria-label="Business card back">
    <div class="back__brand">
      <span class="back__mark"></span>
      <span class="back__name">dorvak</span>
    </div>
    <p class="back__url">www.dorvak-example.nl</p>
  </section>
</body>
</html>
```